Land Buying Company Needs Letterhead for Direct Mail Marketing to Land Owners

We are looking for a professional letterhead that we will be including in our direct mail marketing. We will be sending this to land owners who may be interested in selling or purchasing land.

The letterhead needs to be editable. Headers and footers would look nice, but we are open. We would want it to include our address, website, phone, and email info. For right now the address to use for design purposes would the following:

Address: 415 Bramwell Avenue #600
Dallas, TX 75219
Website - www.quillridgeacres.example
Email - info@quillridgeacres.example
Phone - 866-402-ACRE

I have attached our logo zip file that we just had done on Pixel Guild. Let me know what questions you have, and thank you.

```html
<!DOCTYPE html>
<html lang="en">
<head>
<meta charset="utf-8">
<title>Quillridge Acres Letterhead</title>
<link href="https://fonts.googleapis.com/css2?family=Poppins:wght@400;500;600&display=swap" rel="stylesheet">
<style>
  :root {
    --forest: #46612a;
    --forest-deep: #3a5222;
    --lime: #8dc63f;
    --ink: #2b2b2b;
    --muted: #4a4a4a;
    --paper: #ffffff;
    --backdrop: #eeeeee;
    --map-tint: #f1f2f0;
  }
  * { margin: 0; padding: 0; box-sizing: border-box; }
  html, body { width: 1200px; height: 864px; overflow: hidden; }
  body {
    background: var(--backdrop);
    font-family: "Poppins", sans-serif;
    color: var(--ink);
    position: relative;
  }
  .letterhead {
    position: absolute;
    left: 283px; top: 22px;
    width: 634px; height: 820px;
    background: var(--paper);
    box-shadow: 0 4px 18px rgba(0,0,0,0.12);
    overflow: hidden;
  }
  .top-rule {
    position: absolute; left: 0; top: 0; width: 100%; height: 3px;
    background: var(--forest);
  }
  .world-map {
    position: absolute; left: 40px; top: 40px;
    width: 560px; height: 270px;
    background: radial-gradient(ellipse at 55% 45%, var(--map-tint) 0%, rgba(241,242,240,0.5) 55%, rgba(255,255,255,0) 80%);
  }
  .brand-block {
    position: absolute; left: 73px; top: 0;
    width: 145px; height: 118px;
    background: var(--forest);
    display: flex; align-items: flex-end;
    padding: 0 10px 26px 12px;
  }
  .brand {
    display: flex; align-items: center; gap: 6px;
  }
  .brand-dot {
    width: 18px; height: 18px; border-radius: 50%;
    background: #ffffff;
    flex: none;
  }
  .brand-name {
    font-size: 10px; font-weight: 600; color: var(--lime);
    letter-spacing: 0.2px; line-height: 1; white-space: nowrap;
  }
  .recipient {
    position: absolute; left: 85px; top: 194px;
    font-size: 10.5px; line-height: 14px; color: var(--muted);
  }
  .recipient .name { font-weight: 600; color: var(--ink); }
  .letter-body {
    position: absolute; left: 85px; top: 296px; width: 470px;
    font-size: 10px; line-height: 13.5px; color: var(--ink);
  }
  .letter-body p { margin-bottom: 13px; }
  .letter-body p:last-child { margin-bottom: 0; }
  .signature {
    position: absolute; left: 85px; top: 646px;
    width: 140px; height: 30px;
    background: linear-gradient(90deg, rgba(70,97,42,0.18), rgba(70,97,42,0.05));
    border-radius: 15px;
  }
  .signatory {
    position: absolute; left: 85px; top: 682px;
    font-size: 10.5px; line-height: 14px; color: var(--muted);
  }
  .signatory .name { font-weight: 600; color: var(--ink); }
  .footer-band {
    position: absolute; left: 0; bottom: 8px; width: 100%; height: 72px;
    background: var(--lime);
  }
  .footer-base {
    position: absolute; left: 0; bottom: 0; width: 100%; height: 8px;
    background: var(--forest);
  }
  .contact-bar {
    position: absolute; left: 40px; bottom: 60px;
    width: 560px; height: 34px;
    background: var(--forest-deep);
    border-radius: 17px;
  }
  .contact-row {
    position: absolute; left: 40px; bottom: 14px; width: 560px;
    display: flex; justify-content: space-around;
  }
  .contact-item {
    width: 140px; text-align: center;
    font-size: 7.5px; line-height: 10px; color: var(--forest-deep);
    position: relative;
  }
  .contact-item svg {
    position: absolute; left: 50%; top: -46px; transform: translateX(-50%);
  }
</style>
</head>
<body>
  <main class="letterhead">
    <div class="top-rule"></div>
    <div class="world-map" role="img" aria-label="Faint dotted world map backdrop"></div>

    <div class="brand-block">
      <div class="brand">
        <span class="brand-dot"></span>
        <span class="brand-name">QUILLRIDGE ACRES</span>
      </div>
    </div>

    <section class="recipient">
      <div class="name">Dear Priya</div>
      <div>Senior Executive</div>
      <div>Address goes here. Street, City, Country</div>
      <div>contact@yourmail.com</div>
      <div>000-987-654-321</div>
    </section>

    <section class="letter-body">
      <p>Dear Recipient,</p>
      <p>Write the body of your letter here. To update any of the information in this letter, simply click and start typing!</p>
      <p>Want to customize your color palette? Just go to the Design ribbon, and select Colors from the list. If you choose a color palette that you like, the colors of the header images will update, as will the text colors. Make the document yours!</p>
      <p>Want to change the fonts that are used? That is just as easy to update. Just go to the Design ribbon and choose Fonts from the menu options. You can use a built-in font combination or choose one of your own.</p>
      <p>Lorem ipsum dolor sit amet, consectetur adipisicing elit, sed do eiusmod tempor incididunt ut labore et dolore magna aliqua. Ut enim ad minim veniam, quis nostrud exercitation ullamco laboris nisi ut aliquip ex ea commodo consequat. Duis aute irure dolor in reprehenderit in voluptate velit esse cillum dolore eu fugiat nulla pariatur. Excepteur sint occaecat cupidatat non proident, sunt in culpa qui officia deserunt mollit anim id est laborum.</p>
      <p>Sed ut perspiciatis unde omnis iste natus error sit voluptatem accusantium doloremque laudantium, totam rem aperiam, eaque ipsa quae ab illo inventore veritatis et quasi architecto beatae vitae dicta sunt explicabo. Nemo enim ipsam voluptatem quia voluptas sit aspernatur aut odit veritatis et quasi architecto aut.</p>
    </section>

    <div class="signature" role="img" aria-label="Handwritten signature of Owen Marsh"></div>
    <section class="signatory">
      <div class="name">Owen Marsh</div>
      <div>General Manager</div>
    </section>

    <div class="footer-band"></div>
    <div class="footer-base"></div>
    <div class="contact-bar"></div>

    <footer class="contact-row">
      <div class="contact-item">
        <svg width="12" height="14" viewBox="0 0 12 14"><path d="M6 0a5 5 0 0 0-5 5c0 3.5 5 9 5 9s5-5.5 5-9a5 5 0 0 0-5-5zm0 7a2 2 0 1 1 0-4 2 2 0 0 1 0 4z" fill="#8dc63f"/></svg>
        Address: 415 Bramwell Avenue #600<br>Dallas, TX 75219
      </div>
      <div class="contact-item">
        <svg width="12" height="12" viewBox="0 0 12 12"><circle cx="6" cy="6" r="5" fill="none" stroke="#8dc63f" stroke-width="1.2"/><ellipse cx="6" cy="6" rx="2.2" ry="5" fill="none" stroke="#8dc63f" stroke-width="1"/><line x1="1" y1="6" x2="11" y2="6" stroke="#8dc63f" stroke-width="1"/></svg>
        www.quillridgeacres.example
      </div>
      <div class="contact-item">
        <svg width="14" height="10" viewBox="0 0 14 10"><rect x="0.6" y="0.6" width="12.8" height="8.8" fill="none" stroke="#8dc63f" stroke-width="1.2"/><path d="M1 1l6 5 6-5" fill="none" stroke="#8dc63f" stroke-width="1.2"/></svg>
        info@quillridgeacres.example
      </div>
      <div class="contact-item">
        <svg width="12" height="12" viewBox="0 0 12 12"><path d="M2.5 0.5l2 2.5-1.2 1.5c.8 1.7 2 2.9 3.7 3.7l1.5-1.2 2.5 2-1 2.2C5 11 1 7 .3 1.5z" fill="#8dc63f"/></svg>
        866-402-ACRE
      </div>
    </footer>
  </main>
</body>
</html>
```